Business Card/Logo Design Project

Design the Business card For a psychologist providing relationship workshops, see website draft at www.brightmorrowtalks.com.au.

The background is to be beige with shadows in ivory of the letter "L" as shown on the website noted above.

The words "Kindred Hours" on the front with the first letter of each word in very scrolled lettering and the remaining letters more formal. The front design is to be the logo of the business for use on other items.

The reverse is to show...

client's name
date
time
workshop number
workshop name
and at the bottom "PLEASE BE PUNCTUAL. BRING NOTEPAD & PEN"

Target Market(s)

female, middle-class, educated, introspective

Industry/Entity Type

Business

Requirements
Must have
• see www.brightmorrowtalks.com.au for the design aesthetic - just need you to make it look professional.

cream, beige, grey, chocolate, tan, ivory.

calligraphy shadows as per referenced website

business card back, flyer and postcard to just be background so that I can add text on top through papercrane.

see website for colour-scheme.
Should not have
• not cutesy, pink, or mushy

```html
<!DOCTYPE html>
<html lang="en">
<head>
<meta charset="utf-8">
<title>Kindred Hours — Business Card</title>
<link href="https://fonts.googleapis.com/css2?family=Libre+Baskerville:wght@400;700&display=swap" rel="stylesheet">
<style>
  :root {
    --page: #ffffff;
    --beige: #bfb79e;
    --beige-light: #cdc6ae;
    --beige-dark: #a89f85;
    --shadow: #8f826c;
    --ivory: #f4f1dc;
    --chocolate: #5e4a14;
  }
  html, body {
    margin: 0;
    padding: 0;
    width: 1200px;
    height: 1200px;
    overflow: hidden;
    background: var(--page);
  }
  .canvas {
    position: relative;
    width: 1200px;
    height: 1200px;
  }
  .card {
    position: absolute;
    left: 160px;
    width: 864px;
    background: var(--beige);
    overflow: hidden;
  }
  .card--front {
    top: 64px;
    height: 506px;
  }
  .flourish-field {
    position: absolute;
  }
  .flourish-field--left {
    left: 0;
    top: 0;
    width: 440px;
    height: 506px;
    background:
      radial-gradient(ellipse 55% 70% at 35% 45%, rgba(244,241,220,0.85), rgba(244,241,220,0.35) 45%, rgba(244,241,220,0) 72%),
      radial-gradient(ellipse 60% 40% at 55% 85%, rgba(143,130,108,0.45), rgba(143,130,108,0) 70%);
  }
  .flourish-field--right {
    right: 0;
    top: 110px;
    width: 340px;
    height: 396px;
    background:
      radial-gradient(ellipse 60% 65% at 70% 55%, rgba(244,241,220,0.85), rgba(244,241,220,0.35) 45%, rgba(244,241,220,0) 72%),
      radial-gradient(ellipse 45% 40% at 45% 40%, rgba(143,130,108,0.4), rgba(143,130,108,0) 70%);
  }
  .brand {
    position: absolute;
    left: 0;
    right: 0;
    top: 262px;
    text-align: center;
    font-family: "Libre Baskerville", serif;
    font-weight: 400;
    color: var(--chocolate);
  }
  .brand-name {
    margin: 0;
    display: inline-block;
    position: relative;
    font-family: inherit;
    font-weight: 400;
    font-size: 74px;
    line-height: 1;
  }
  .brand-suffix {
    position: absolute;
    right: 0;
    top: 100%;
    margin-top: 2px;
    font-size: 17px;
    font-weight: 400;
    line-height: 1;
  }
  .card--back {
    top: 622px;
    height: 556px;
    font-family: "Libre Baskerville", serif;
    font-weight: 700;
  }
  .back-title {
    position: absolute;
    top: 18px;
    left: 0;
    right: 0;
    margin: 0;
    text-align: center;
    font-size: 36px;
    color: var(--chocolate);
    font-weight: 700;
  }
  .field-row {
    position: absolute;
    left: 27px;
    right: 24px;
    display: flex;
    align-items: flex-end;
    font-size: 29px;
    color: var(--ivory);
  }
  .field-label {
    white-space: nowrap;
    line-height: 1;
  }
  .field-line {
    flex: 1;
    border-bottom: 1.5px solid var(--ivory);
    margin: 0 4px 4px 4px;
    opacity: 0.9;
  }
  .field-row--client { top: 116px; }
  .field-row--date { top: 214px; }
  .field-row--workshop { top: 310px; }
  .field-row--blank {
    top: 404px;
    height: 0;
    border-bottom: 1.5px solid var(--ivory);
    opacity: 0.9;
  }
  .back-note {
    position: absolute;
    left: 0;
    right: 0;
    top: 456px;
    margin: 0;
    text-align: center;
    font-size: 29px;
    color: var(--chocolate);
  }
</style>
</head>
<body>
<main class="canvas">
  <section class="card card--front">
    <div class="flourish-field flourish-field--left" role="img" aria-label="Large ivory calligraphic letter flourish with soft shadow on the left of the card"></div>
    <div class="flourish-field flourish-field--right" role="img" aria-label="Large ivory calligraphic letter flourish with soft shadow on the right of the card"></div>
    <div class="brand">
      <h1 class="brand-name">Kindred Hours<span class="brand-suffix">.com.au</span></h1>
    </div>
  </section>

  <section class="card card--back">
    <h2 class="back-title">Appointment/ Workshop</h2>
    <div class="field-row field-row--client">
      <span class="field-label">Client Name</span><span class="field-line"></span>
    </div>
    <div class="field-row field-row--date">
      <span class="field-label">Date(s)</span><span class="field-line"></span>
      <span class="field-label">Time</span><span class="field-line"></span>
    </div>
    <div class="field-row field-row--workshop">
      <span class="field-label">Workshop No’ &amp; Name</span><span class="field-line"></span>
    </div>
    <div class="field-row field-row--blank"></div>
    <p class="back-note">Please be Punctual. Bring a Notepad &amp; Pen.</p>
  </section>
</main>
</body>
</html>
```